Consulting Company needs business card design

We need a business card design for a new consulting and business solutions company based in Bermuda called Corvane Holdings Limited. Looking for a double sided business card with one side only including the company logo thats attached and the other including contact information. Logo contains blue and turquoise colors and is fine to be on both sides of the card.
Contact Information for Business Card
Corvane Holdings Limited
P.O. Box KR318
Pemberly KR LT
Bermuda
Name: Marcus Telford
Position: Director
Telephone: 1 441 732 4590
Email: mtelford@corvane.bm
Website: www.corvane.bm

```html
<!DOCTYPE html>
<html lang="en">
<head>
<meta charset="utf-8">
<title>Corvane Holdings Limited – Business Cards</title>
<link href="https://fonts.googleapis.com/css2?family=Source+Sans+3:wght@400;600;700&display=swap" rel="stylesheet">
<style>
  :root {
    --backdrop: #3a3a3a;
    --card: #ffffff;
    --brand-blue: #2ea3dc;
    --ink-blue: #3a9fd6;
    --faint-mark: #e3f3f7;
  }
  * { margin: 0; padding: 0; box-sizing: border-box; }
  html, body { width: 1200px; height: 801px; overflow: hidden; }
  body {
    background: var(--backdrop);
    font-family: "Source Sans 3", Arial, sans-serif;
    position: relative;
  }
  .card {
    position: absolute;
    top: 273px;
    width: 450px;
    height: 257px;
    background: var(--card);
    border-radius: 18px;
    overflow: hidden;
    box-shadow: 0 10px 24px rgba(0,0,0,.45);
  }
  .card--front { left: 133px; }
  .card--back { left: 620px; }

  .corner-mark {
    position: absolute;
    right: -70px;
    bottom: -70px;
    width: 180px;
    height: 180px;
    border-radius: 50%;
    background: var(--faint-mark);
  }

  .brand {
    position: absolute;
    display: flex;
    align-items: center;
    gap: 12px;
    color: var(--brand-blue);
    font-weight: 600;
  }
  .brand__dot {
    border-radius: 50%;
    background: var(--brand-blue);
    flex: none;
  }
  .brand__name { line-height: 1; text-transform: uppercase; }
  .brand__line { display: block; }

  .card--front .brand { left: 76px; top: 88px; }
  .card--front .brand__dot { width: 66px; height: 66px; }
  .card--front .brand__line--main { font-size: 40px; letter-spacing: 1px; }
  .card--front .brand__line--sub { font-size: 17px; letter-spacing: 3.2px; margin-top: 4px; }

  .card--back .brand { left: 100px; top: 26px; gap: 10px; }
  .card--back .brand__dot { width: 48px; height: 48px; }
  .card--back .brand__line--main { font-size: 31px; letter-spacing: 1px; }
  .card--back .brand__line--sub { font-size: 13px; letter-spacing: 2.5px; margin-top: 3px; }

  .person { position: absolute; left: 28px; top: 132px; color: var(--ink-blue); }
  .person__name { font-size: 16px; font-weight: 700; letter-spacing: .6px; text-transform: uppercase; }
  .person__role { font-size: 14px; font-weight: 600; margin-top: 2px; }

  .contacts {
    position: absolute;
    left: 226px;
    top: 133px;
    list-style: none;
    color: var(--ink-blue);
    font-size: 13.5px;
    line-height: 18.4px;
  }
  .contacts li { display: flex; align-items: center; gap: 6px; white-space: nowrap; }
  .contacts svg { width: 10px; height: 10px; flex: none; }
</style>
</head>
<body>
  <section class="card card--front">
    <div class="corner-mark" aria-hidden="true"></div>
    <div class="brand">
      <span class="brand__dot"></span>
      <span class="brand__name">
        <span class="brand__line brand__line--main">Corvane</span>
        <span class="brand__line brand__line--sub">Holdings Limited</span>
      </span>
    </div>
  </section>

  <section class="card card--back">
    <div class="corner-mark" aria-hidden="true"></div>
    <div class="brand">
      <span class="brand__dot"></span>
      <span class="brand__name">
        <span class="brand__line brand__line--main">Corvane</span>
        <span class="brand__line brand__line--sub">Holdings Limited</span>
      </span>
    </div>

    <div class="person">
      <p class="person__name">Marcus Telford</p>
      <p class="person__role">Director</p>
    </div>

    <ul class="contacts">
      <li>
        <svg viewBox="0 0 10 10"><circle cx="5" cy="5" r="5" fill="#3a9fd6"/><path d="M2.5 6.5 L7.5 3.5 L5.5 7.5 Z" fill="#fff"/></svg>
        P.O. Box KR318
      </li>
      <li>
        <svg viewBox="0 0 10 10"><circle cx="5" cy="5" r="5" fill="#3a9fd6"/><circle cx="5" cy="4.2" r="1.6" fill="#fff"/><path d="M3.6 5 L5 8 L6.4 5 Z" fill="#fff"/></svg>
        Pemberly KR LT, Bermuda
      </li>
      <li>
        <svg viewBox="0 0 10 10"><circle cx="5" cy="5" r="5" fill="#3a9fd6"/><rect x="2.6" y="3" width="4.8" height="4.2" rx="1" fill="#fff"/></svg>
        1 441 732 4590
      </li>
      <li>
        <svg viewBox="0 0 10 10"><circle cx="5" cy="5" r="5" fill="#3a9fd6"/><rect x="2.5" y="3.3" width="5" height="3.4" fill="#fff"/><path d="M2.5 3.3 L5 5.2 L7.5 3.3" stroke="#3a9fd6" stroke-width=".7" fill="none"/></svg>
        mtelford@corvane.bm
      </li>
      <li>
        <svg viewBox="0 0 10 10"><circle cx="5" cy="5" r="5" fill="#3a9fd6"/><circle cx="5" cy="5" r="2.6" fill="none" stroke="#fff" stroke-width=".8"/><path d="M2.4 5 H7.6 M5 2.4 V7.6" stroke="#fff" stroke-width=".6"/></svg>
        www.corvane.bm
      </li>
    </ul>
  </section>
</body>
</html>
```